Flyer / marketing email used to solicate work for specialized tree removal equipment.

I'm looking for a flyer for door to door and direct mail distributon. Please utilize as much of the following verbiage as possible...

Breaking news!¿the only 170' grapple crane in use in North American is coming to your neighborhood This revolutionary technology will be in your area for a limited time. Our equipment allows to us accomplish the most challenging tree scenarios with no climber, limited personnel, and amazing efficiency.

This innovation has completely changed the cost of hazardous removals. Call now to get the most competitive estimate yet.

This technology is so limited and in high demand that it can only be in your area for a short time before it has to move on. Get on the list today, it may be months before it makes another round to your neighborhood. ¿

Target Market(s)

Flyers will be delivered in a high end residential neighborhood. Distribution will be on heavy stock and via email.

Colors

Designer to choose colors to be used in the design.

Requirements
Must have
• My logo. Pictures of the crane equipment. Pictures of other tree equipment.
• I'd like a two sided 4" x 5.5" mailer.
• I have permissions to utilize content from the sample one fold flyers I have uploaded.
• I'd like a majority of the content of the Vortalix (aka. Plover limb sample). The light background of the 842 Boughs sample.
• A "BLACK FRIDAY SALE" theme would be awesome.
Nice to have
• Old time breaking news headline married with a high tech innovative feel
• OR
• BLACK FRIDAY SALE theme.

```html
<!DOCTYPE html>
<html lang="en">
<head>
<meta charset="utf-8">
<title>Allhours Arbor Co – Crane Removal Mailer</title>
<link href="https://fonts.googleapis.com/css2?family=Oswald:wght@400;500&family=Ubuntu:wght@400;500&display=swap" rel="stylesheet">
<style>
  :root{
    --canvas:#b9b9b9;
    --paper:#ffffff;
    --forest:#33581f;
    --green:#17873f;
    --lime:#9acd32;
    --ink:#111111;
    --muted:#555555;
  }
  *{margin:0;padding:0;box-sizing:border-box}
  html,body{width:902px;height:1200px;overflow:hidden}
  body{background:var(--canvas);position:relative;font-family:"Ubuntu",sans-serif;color:var(--ink)}
  .side-label{position:absolute;font-family:"Oswald",sans-serif;font-weight:500;font-size:26px;letter-spacing:.5px;
    transform:rotate(-90deg);transform-origin:left top;color:#111}
  .side-label--front{left:22px;top:360px}
  .side-label--back{left:22px;top:945px}
  .card{position:absolute;left:70px;width:780px;height:566px;background:var(--paper);overflow:hidden;
    box-shadow:0 2px 6px rgba(0,0,0,.35)}
  .card--front{top:22px}
  .card--back{top:612px}
  .card svg.shapes{position:absolute;left:0;top:0}
  .abs{position:absolute}
  .brand{display:flex;align-items:center;gap:6px;font-family:"Ubuntu",sans-serif;font-weight:500;color:var(--forest)}
  .brand-dot{width:14px;height:14px;border-radius:50%;background:var(--forest)}
  .brand-sub{font-size:10px;color:var(--muted);letter-spacing:1px;text-align:center}
  .tagline{font-family:"Ubuntu",sans-serif;color:#222;font-size:22px;text-align:center}
  .headline{font-family:"Oswald",sans-serif;font-weight:500}
  .body-copy{font-size:13.6px;line-height:18.8px;text-align:right}
  .body-copy b{font-weight:500}
  .green-copy{font-size:13.6px;line-height:18.8px;color:var(--green);font-weight:500;text-align:justify;text-align-last:right}
  .white{color:#fff}
</style>
</head>
<body>
  <div class="side-label side-label--front">FRONT SIDE</div>
  <div class="side-label side-label--back">BACK SIDE</div>

  <!-- FRONT -->
  <section class="card card--front">
    <svg class="shapes" width="780" height="566" viewBox="0 0 780 566">
      <defs>
        <linearGradient id="craneScene" x1="0" y1="0" x2="0" y2="1">
          <stop offset="0" stop-color="#6aa6e0"/>
          <stop offset=".45" stop-color="#4f7d3a"/>
          <stop offset="1" stop-color="#6cc04a"/>
        </linearGradient>
      </defs>
      <polygon points="310,0 780,0 780,12 316,12" fill="var(--green)"/>
      <polygon points="306,0 318,0 491,349 478,349" fill="var(--green)"/>
      <g role="img" aria-label="Photo of the grapple crane truck reaching over a large house and lawn">
        <polygon points="0,0 306,0 478,349 0,349" fill="url(#craneScene)"/>
      </g>
      <polygon points="390,150 780,150 780,221 424,221" fill="var(--forest)"/>
      <rect x="0" y="349" width="240" height="144" fill="var(--forest)"/>
      <polygon points="240,349 408,349 408,493 240,493 226,421" fill="var(--lime)"/>
      <rect x="14" y="358" width="222" height="126" fill="none" stroke="#fff" stroke-width="2" stroke-dasharray="7 5"/>
      <rect x="0" y="499" width="780" height="67" fill="var(--forest)"/>
      <polygon points="0,499 280,499 300,566 0,566" fill="var(--lime)"/>
      <polygon points="280,499 500,499 530,566 300,566" fill="var(--green)"/>
      <polygon points="500,499 520,499 545,566 530,566" fill="var(--lime)"/>
    </svg>

    <div class="abs" style="left:400px;top:44px;width:160px">
      <div class="brand" style="justify-content:center;font-size:16px"><span class="brand-dot"></span>Allhours Arbor Co</div>
      <div class="brand-sub" style="margin-top:4px">- 855.LIMB.365 -</div>
    </div>
    <div class="abs tagline" style="left:560px;top:28px;width:220px;font-size:21px">CRANE ASSISTED</div>
    <div class="abs headline" style="left:560px;top:62px;width:220px;text-align:center;font-size:30px">855-<span style="color:var(--green)">LIMB</span>-365</div>
    <div class="abs tagline" style="left:560px;top:106px;width:220px;font-size:21px">TREE REMOVAL</div>

    <div class="abs headline" style="left:420px;top:160px;width:355px;text-align:right;font-size:36px;color:var(--lime);line-height:50px">TITAN REACH IN ACTION</div>

    <p class="abs body-copy" style="left:470px;top:228px;width:294px">
      <b>the only 170' grapple crane in use in North American is coming to your neighborhood This revolutionary technology will be in your area for a limited time.</b> Our equipment allows to us accomplish the most challenging tree scenarios with no climber, limited personnel, and amazing efficiency.
    </p>
    <p class="abs green-copy" style="left:425px;top:386px;width:339px">
      This technology is so limited and in high demand that it can only be in your area for a short time before it has to move on. Get on the list today, it may be months before it makes another round to your neighborhood.
    </p>

    <div class="abs white" style="left:14px;top:362px;width:222px;text-align:center">
      <div style="font-size:14px">Returning customers</div>
      <div style="font-size:25px;line-height:28px;margin-top:2px">Call for</div>
      <div style="font-size:28px;font-weight:500;line-height:30px">10% OFF</div>
      <div style="font-size:14px;line-height:19px;margin-top:2px">any previously quoted<br>tree removal.</div>
    </div>
    <div class="abs" style="left:240px;top:367px;width:168px;text-align:center;font-size:16px;line-height:21px;font-weight:500;color:var(--ink)">
      This innovation has completely changed the cost of hazardous removals.
    </div>

    <div class="abs headline" style="left:22px;top:512px;font-size:28px;color:var(--green);line-height:40px">CALL NOW <span class="white">855-LIMB-365</span></div>
    <div class="abs white" style="left:300px;top:512px;width:220px;text-align:center;font-size:15.5px;line-height:21px;font-weight:500">to get the most competitive estimate yet.</div>
    <div class="abs headline white" style="left:535px;top:514px;width:235px;text-align:right;font-size:18px;line-height:26px;display:flex;align-items:center;justify-content:flex-end;gap:6px">
      <svg width="14" height="14" viewBox="0 0 14 14" aria-hidden="true"><g fill="none" stroke="#fff" stroke-width="1.2"><circle cx="7" cy="7" r="6"/><ellipse cx="7" cy="7" rx="2.6" ry="6"/><line x1="1" y1="7" x2="13" y2="7"/></g></svg>
      www.allhoursarbor.com
    </div>
  </section>

  <!-- BACK -->
  <section class="card card--back">
    <svg class="shapes" width="780" height="566" viewBox="0 0 780 566">
      <defs>
        <linearGradient id="roofScene" x1="0" y1="0" x2="0" y2="1">
          <stop offset="0" stop-color="#7fb2e0"/>
          <stop offset=".5" stop-color="#5a6d48"/>
          <stop offset="1" stop-color="#6f6a66"/>
        </linearGradient>
        <linearGradient id="pineScene" x1="0" y1="0" x2="0" y2="1">
          <stop offset="0" stop-color="#5c9be0"/>
          <stop offset=".7" stop-color="#8ebbe8"/>
          <stop offset="1" stop-color="#3f6a2e"/>
        </linearGradient>
      </defs>
      <polygon points="0,0 462,0 460,12 0,12" fill="var(--forest)"/>
      <polygon points="466,0 474,0 364,566 356,566" fill="var(--green)"/>
      <g role="img" aria-label="Panoramic photo of the crane boom extending over a house roof">
        <rect x="0" y="20" width="462" height="146" fill="url(#roofScene)"/>
      </g>
      <polygon points="0,172 430,172 354,566 0,566" fill="var(--forest)"/>
      <rect x="24" y="323" width="166" height="227" fill="#fff"/>
      <g role="img" aria-label="Photo of the crane grabbing a tall pine tree beside a house">
        <rect x="28" y="327" width="158" height="219" fill="url(#pineScene)"/>
      </g>
      <rect x="200" y="460" width="52" height="82" fill="#fff"/>
      <rect x="206" y="466" width="40" height="70" fill="#1f4f7a"/>
      <circle cx="300" cy="500" r="40" fill="#d9d9d9"/>
      <circle cx="300" cy="500" r="32" fill="#8a8a8a"/>
      <rect x="672" y="28" width="80" height="90" fill="none" stroke="#111" stroke-width="2"/>
    </svg>

    <div class="abs headline" style="left:23px;top:178px;width:400px;font-size:20px;line-height:23px;color:var(--lime);font-weight:400">With 170 feet reach, no tree is too far away we can reach most backyard trees from the front yard.</div>
    <p class="abs white" style="left:23px;top:232px;width:385px;font-size:12.6px;line-height:16.4px;font-weight:500">
      Titan Reach is the only tree removal truck that can do the job without a man ever leaving the ground. " Titan Reach" extends out with an outstanding 170 ft of reach and grabs the tree, then cuts it and safely lowers it to the ground. Tree work has never been safer or more affrotable in Jacksonville
    </p>
    <div class="abs" style="left:196px;top:324px;width:160px;text-align:center">
      <div class="headline" style="font-size:26px;color:var(--lime);line-height:32px;font-weight:400">CALL TODAY</div>
      <div class="headline white" style="font-size:26px;line-height:36px;font-weight:400">855-LIMB-365</div>
      <div class="white" style="font-size:14.4px;line-height:18.5px;font-weight:500;margin-top:2px">to witness this amazing piece of equipment in action</div>
    </div>

    <div class="abs" style="left:500px;top:60px;width:140px">
      <div class="brand" style="justify-content:center;font-size:13px"><span class="brand-dot" style="width:11px;height:11px"></span>Allhours Arbor Co</div>
      <div class="brand-sub" style="margin-top:3px;font-size:8.5px">- 855.LIMB.365 -</div>
    </div>
  </section>
</body>
</html>
```